Brell Harbor Company Business Cards

Front and Back Business Card - logo and text setup - cool design. I need workable photoshop or illustrator files so I can setup each employee card with design that is created
Updates

Hi everyone, thank you for the great entries. Please no more white and blue cards - there are so many already - black and silver only now please. thanks!

Target Market(s)

Construction Industry - Facility Managers

Industry/Entity Type

Construction

Contact Information for Business Card

I really like contemporary simplistic looks - clean neat....not opposed to seeing some black backrounds

Requirements
Must have
• Logo/website address with design on front only - www.brellharbor-example.com (logo attached)
• Back:
• Name/Title/Company Address/Phone/email address
Nice to have
• Cool design
Should not have
• Nothing gimmicky like Fire or Water - since we are a Fire Protection company - it has all been done

```html
<!DOCTYPE html>
<html lang="en">
<head>
<meta charset="utf-8">
<title>Brell Harbor Company Business Cards</title>
<link href="https://fonts.googleapis.com/css2?family=Open+Sans:wght@400;600;800&display=swap" rel="stylesheet">
<style>
  :root {
    --stage: #2b2b2d;
    --card: #1c1c1e;
    --card-edge: #2a2a2c;
    --silver: #b9b9bc;
    --navy: #3c4f94;
    --accent: #e8513a;
    --ink: #f2f2f2;
  }
  html, body {
    margin: 0;
    padding: 0;
    width: 1200px;
    height: 874px;
    overflow: hidden;
    background: var(--stage);
    font-family: "Open Sans", Arial, sans-serif;
  }
  .stage {
    position: relative;
    width: 1200px;
    height: 874px;
  }
  .card {
    position: absolute;
    left: 280px;
    width: 640px;
    height: 366px;
    border-radius: 22px;
    background-color: var(--card);
    background-image: radial-gradient(circle, rgba(255,255,255,0.05) 1px, transparent 1.4px);
    background-size: 8px 8px;
    box-shadow: 0 10px 30px rgba(0,0,0,0.45), inset 0 0 0 1px var(--card-edge);
  }
  .card-front { top: 50px; }
  .card-back { top: 440px; }

  .front-name {
    position: absolute;
    left: 0;
    right: 0;
    top: 138px;
    text-align: center;
    font-size: 74px;
    font-weight: 800;
    letter-spacing: -1px;
    color: var(--silver);
  }

  .back-name {
    position: absolute;
    right: 52px;
    top: 48px;
    font-size: 34px;
    font-weight: 800;
    letter-spacing: -0.5px;
    color: var(--navy);
  }

  .person {
    position: absolute;
    left: 48px;
    top: 208px;
    color: var(--ink);
    font-size: 17px;
    line-height: 1.35;
  }
  .person-name {
    color: var(--accent);
    font-size: 26px;
    font-weight: 600;
    margin-bottom: 2px;
  }

  .contact {
    position: absolute;
    left: 300px;
    top: 252px;
    list-style: none;
    margin: 0;
    padding: 0;
    color: var(--ink);
    font-size: 16px;
    line-height: 23px;
  }
  .contact li {
    display: flex;
    align-items: center;
    gap: 10px;
  }
  .contact svg {
    width: 14px;
    height: 14px;
    fill: var(--accent);
    flex: none;
  }
</style>
</head>
<body>
<main class="stage">
  <section class="card card-front" aria-label="Card front">
    <div class="front-name">Brell Harbor</div>
  </section>

  <section class="card card-back" aria-label="Card back">
    <div class="back-name">Brell Harbor</div>

    <div class="person">
      <div class="person-name">Dana Whitfield</div>
      <div class="person-title">CEO/Founder</div>
      <div class="person-street">48 Lantern Row</div>
      <div class="person-city">Millbrook, NY 10000</div>
    </div>

    <ul class="contact">
      <li>
        <svg viewBox="0 0 16 16" aria-hidden="true"><path d="M4 1.5l2.2 3-1.3 1.6c.8 1.8 2.2 3.2 4 4l1.6-1.3 3 2.2-1.2 2.5C7 13.2 2.8 9 2.3 3z"/></svg>
        <span>(555) 014-2870</span>
      </li>
      <li>
        <svg viewBox="0 0 16 16" aria-hidden="true"><rect x="4" y="1" width="8" height="4"/><rect x="1" y="6" width="14" height="6" rx="1"/><rect x="4" y="10" width="8" height="5"/></svg>
        <span>(555) 014-2871</span>
      </li>
      <li>
        <svg viewBox="0 0 16 16" aria-hidden="true"><path d="M1 3h14v10H1z M1.5 3.5L8 9l6.5-5.5" stroke="#1c1c1e" stroke-width="1.2"/></svg>
        <span>info@brellharbor-example.com</span>
      </li>
      <li>
        <svg viewBox="0 0 16 16" aria-hidden="true"><circle cx="8" cy="8" r="7"/><path d="M1 8h14M8 1c-3 3.5-3 10.5 0 14M8 1c3 3.5 3 10.5 0 14" stroke="#1c1c1e" stroke-width="1" fill="none"/></svg>
        <span>www.brellharbor-example.com</span>
      </li>
    </ul>
  </section>
</main>
</body>
</html>
```